Harlow Ridge Growers and Nursery needs a business street sign.

I have three businesses located at the same address: The Harlow Ridge Growers & Nursery, The Bramble Nook, and The Quarry Commons. I am looking for a 4’ x 8’ street sign to represent all three businesses as one retail experience. It needs to be eye catching yet simple enough that people can fully read it while driving by. I have logos for the greenhouse and village however I do not have anything for The Bramble Nook. I’m looking for some type of font that’s similar or in between the two attached logos for The Bramble Nook.

• Horizontal Sign, Eye catching, yet simple design so people see it while driving by.
• Horizontal Sign
• I’m open to the design being both vertical and horizontal. Please provide both options

```html
<!DOCTYPE html>
<html lang="en">
<head>
<meta charset="utf-8">
<title>Harlow Ridge Growers &amp; Nursery – Street Sign</title>
<link rel="stylesheet" href="https://fonts.googleapis.com/css2?family=Yellowtail&family=Montserrat:wght@600&display=swap">
<style>
  :root {
    --page: #ffffff;
    --maroon: #722f37;
    --wine: #7e2226;
    --rust: #8f2c25;
    --green: #006b3f;
    --sky: #d4eef6;
    --mint: #dcf8ea;
    --cream: #f1efe0;
    --blush: #f2e8e4;
    --meadow: #7f9450;
  }
  html, body {
    margin: 0;
    width: 1200px;
    height: 1200px;
    overflow: hidden;
    background: var(--page);
  }
  .sign {
    position: absolute;
    left: 65px;
    top: 332px;
    width: 1070px;
    height: 535px;
    overflow: hidden;
    background:
      linear-gradient(to bottom, rgba(255,255,255,0) 0%, rgba(255,255,255,0) 80%, rgba(200,210,160,.6) 88%, var(--meadow) 100%),
      radial-gradient(circle at 25% 20%, #ffffff 0, rgba(255,255,255,0) 18%),
      radial-gradient(ellipse at 20% 55%, var(--blush) 0, rgba(242,232,228,0) 45%),
      linear-gradient(160deg, var(--sky) 0%, var(--mint) 45%, var(--cream) 70%, var(--cream) 100%);
  }
  .brand {
    position: absolute;
    margin: 0;
    font-family: "Yellowtail", cursive;
    font-weight: 400;
    text-align: center;
    line-height: 1;
  }
  .brand--growers {
    left: 110px;
    top: 60px;
    width: 480px;
    font-size: 62px;
    color: var(--green);
  }
  .brand--commons {
    left: 110px;
    top: 385px;
    width: 480px;
    font-size: 66px;
    color: var(--rust);
  }
  .brand--nook {
    left: 690px;
    top: 170px;
    width: 370px;
    font-size: 82px;
    color: var(--wine);
  }
  .divider {
    position: absolute;
    background: var(--maroon);
  }
  .divider--horizontal {
    left: 115px;
    top: 266px;
    width: 439px;
    height: 5px;
  }
  .divider--vertical {
    left: 667px;
    top: 48px;
    width: 5px;
    height: 440px;
  }
</style>
</head>
<body>
  <main class="sign">
    <h1 class="brand brand--growers">The Harlow Ridge Growers &amp; Nursery</h1>
    <div class="divider divider--horizontal"></div>
    <h2 class="brand brand--commons">The Quarry Commons</h2>
    <div class="divider divider--vertical"></div>
    <h2 class="brand brand--nook">The Bramble Nook</h2>
  </main>
</body>
</html>
```